Biz card, letterhead, envelopes for massage business
Massage Business for people and for Equine (horses)
Biz card, letterhead, envelopes for massage business - Massage Therapy
Use same font as used in my logo
simular to my logo
Modern
Marla Kessin
Certified Massage Therapist
P.O. Box 871, Auburn, CA 95718
marlakessin@quillpost.net
I provide massage for people and for horses. We need to creatively put the information on the back of the card. Of course we don't want to say "Human"..... when refering to horse we call it Equine Massage.
Human Massage Therapy.....Swedish, Deep Tissue, Relaxation, Hot Stone, On-Site Chair Massage Equine Massage Therapy...... Stridolan Certified Pellridge Method Relieves muscle pain, enhances performance, reduces inflamation, enhances muscle tone, increases endorphines - a horses natural pain killers For both : Relax Relieve Rejuvenate

```html
<!DOCTYPE html>
<html lang="en">
<head>
<meta charset="utf-8">
<title>Even Keel Bodywork – Business Card</title>
<link href="https://fonts.googleapis.com/css2?family=Raleway:wght@400;500;600&family=Open+Sans:ital,wght@0,400;0,600;1,400&display=swap" rel="stylesheet">
<style>
  :root {
    --bg: #e4e5e6;
    --card: #ffffff;
    --green: #8fae5a;
    --green-dark: #6f9140;
    --brown: #6b3a17;
    --ink: #4a4a4a;
    --ink-soft: #777777;
  }
  * { box-sizing: border-box; margin: 0; padding: 0; }
  html, body { width: 1200px; height: 984px; overflow: hidden; }
  body {
    background: var(--bg);
    font-family: "Open Sans", sans-serif;
    color: var(--ink);
    position: relative;
  }
  .card {
    position: absolute;
    left: 280px;
    width: 640px;
    height: 366px;
    background: var(--card);
    border-radius: 22px;
    box-shadow: 0 6px 18px rgba(0,0,0,0.18);
    overflow: hidden;
  }
  .card--back { top: 80px; }
  .card--front { top: 520px; }

  /* Back side */
  .services {
    position: absolute;
    inset: 0;
    display: flex;
    flex-direction: column;
    align-items: center;
    justify-content: center;
    text-align: center;
    padding: 0 50px;
    font-size: 13px;
    line-height: 1.45;
  }
  .services__heading {
    font-family: "Raleway", sans-serif;
    font-weight: 600;
    color: var(--green-dark);
    font-size: 15px;
  }
  .services__list { margin-bottom: 12px; }
  .services__note { margin-top: 10px; }
  .services__tagline {
    font-family: "Raleway", sans-serif;
    font-weight: 600;
    color: var(--green-dark);
    font-size: 15px;
  }

  /* Front side */
  .swoosh { position: absolute; inset: 0; }
  .brand {
    position: absolute;
    top: 68px;
    left: 0;
    right: 0;
    display: flex;
    align-items: center;
    justify-content: center;
    gap: 12px;
  }
  .brand__dot {
    width: 22px; height: 22px;
    border-radius: 50%;
    background: var(--green);
  }
  .brand__name {
    font-family: "Raleway", sans-serif;
    font-weight: 500;
    font-size: 30px;
    letter-spacing: 2px;
    color: var(--brown);
    text-transform: uppercase;
  }
  .details {
    position: absolute;
    top: 176px;
    left: 250px;
    display: flex;
    gap: 18px;
    font-size: 11.5px;
    line-height: 1.55;
  }
  .person { text-align: right; }
  .person__name {
    font-family: "Raleway", sans-serif;
    font-weight: 600;
    color: var(--brown);
    font-size: 13px;
  }
  .person__title { font-style: italic; color: var(--ink-soft); }
  .divider { width: 1px; background: var(--green); }
  .contact { list-style: none; }
  .contact li { display: flex; align-items: center; gap: 6px; }
  .contact svg { flex: none; }
</style>
</head>
<body>

  <section class="card card--back" aria-label="Card back">
    <div class="services">
      <p class="services__heading">Human Massage Therapy</p>
      <p class="services__list">Swedish | Deep Tissue | Relaxation | Hot Stone | On-Site Chair Massage</p>
      <p class="services__heading">Equine Massage Therapy</p>
      <p>Stridolan Certified | Pellridge Method</p>
      <p>Relieves muscle pain, enhances performance, reduces inflammation,<br>enhances muscle tone, increases endorphins – a horse's natural pain killers</p>
      <p class="services__note">For both</p>
      <p class="services__tagline">Relax Relieve Rejuvenate</p>
    </div>
  </section>

  <section class="card card--front" aria-label="Card front">
    <svg class="swoosh" viewBox="0 0 640 366" width="640" height="366" aria-hidden="true">
      <path d="M0 140 C170 160 340 240 500 366 L0 366 Z" fill="var(--green)"/>
      <path d="M0 166 C170 186 330 262 470 366 L0 366 Z" fill="#ffffff"/>
      <path d="M0 182 C160 205 310 280 440 366 L0 366 Z" fill="var(--brown)"/>
      <path d="M360 366 C450 320 550 300 640 300 L640 366 Z" fill="var(--green)"/>
      <path d="M400 366 C480 334 560 322 640 322 L640 366 Z" fill="#ffffff" opacity="0.35"/>
    </svg>

    <div class="brand">
      <span class="brand__dot"></span>
      <span class="brand__name">Even Keel Bodywork</span>
    </div>

    <div class="details">
      <div class="person">
        <p class="person__name">Marla Kessin</p>
        <p class="person__title">Certified Massage Therapist</p>
        <p>P.O. Box 871, Auburn, CA 95718</p>
      </div>
      <span class="divider"></span>
      <ul class="contact">
        <li>
          <svg width="12" height="12" viewBox="0 0 12 12" aria-hidden="true"><circle cx="6" cy="6" r="6" fill="var(--green)"/><path d="M4 3.2 L5 5 L4.5 5.6 C5 6.6 5.6 7.2 6.4 7.5 L7 7 L8.8 8 L8.2 9 C6 9 3 6 3 3.8 Z" fill="#fff"/></svg>
          530-555-0147
        </li>
        <li>
          <svg width="12" height="12" viewBox="0 0 12 12" aria-hidden="true"><circle cx="6" cy="6" r="6" fill="var(--green)"/><rect x="3" y="4" width="6" height="4" fill="none" stroke="#fff" stroke-width="0.9"/><path d="M3 4 L6 6.3 L9 4" fill="none" stroke="#fff" stroke-width="0.9"/></svg>
          marlakessin@quillpost.net
        </li>
        <li>
          <svg width="12" height="12" viewBox="0 0 12 12" aria-hidden="true"><circle cx="6" cy="6" r="6" fill="var(--green)"/><circle cx="6" cy="6" r="3" fill="none" stroke="#fff" stroke-width="0.9"/><path d="M3 6 H9 M6 3 V9" stroke="#fff" stroke-width="0.7"/></svg>
          www.evenkeelbodywork.com
        </li>
      </ul>
    </div>
  </section>

</body>
</html>
```